Beautiful & Elegant Digital Brochure Needed For Luxury Real Estate Development

Hello,

Our company is seeking a beautiful design for our real estate development that is currently being launched.

About The Project:
Development Name - Willow Crest Estate
Location - Charleston, S.C.
Low-Country Southern Style Architecture
Google "low-country" Charleston, SC to get an idea of the unique culture of the city
Google "willow crest tree" Charleston, SC to understand the branding

Other Digital Brochures that we love

http://www.fernvalehotels.example/cedarhollow/wp-content/uploads/sites/6/2014/08/adventures-brochure.pdf

Why we like it... We love the classy feeling the brochure portrays by using unique fonts and backgrounds (burlap textures). We also love the images that represent a "low-country" vibe.

Requirements:
1. We will be providing all of the content (attached)

2. Please use plenty of southern low-country stock images from PixelVaultStock (we have a subscription so just use the watermarked images unless you have full permissions)

3. Do not copy the Cedar Hollow brochure - create a unique vision that fits in to the low-country and southern vibe

4. Attached is our logos

The font we like to use is - Caslon Antique / italic
Thank you!

Project Deadline Extended Reason: We've added more design information and we need to get more designers to participate. Added Monday, May 30, 2016

Target Market(s)

High net worth individuals - each homesite will be over 6 million dollars USD

Industry/Entity Type

Real Estate Development

Font styles to use
Script
Other font styles liked:
• Caslon Antique & Italic

Colors
abd036
00a990
acd036
9bcb3c
33b8a4
86cfc6
cfeae6

Requirements
Must have
• low country feeling
Nice to have
• burlap, wood backgrounds
Should not have
• Should NOT be corporate. This brochure is for multi-millionaire home buyers and investors. They are seeking simple, beautiful, quiet, serene, and southern lifestyles on the Intracoastal waterway on Marley Isle, Charleston, South Carolina.

```html
<!DOCTYPE html>
<html lang="en">
<head>
<meta charset="utf-8">
<title>Willow Crest Estate – Charleston's Attractions</title>
<link href="https://fonts.googleapis.com/css2?family=EB+Garamond:ital,wght@0,400;0,500;1,400;1,500;1,600&family=Parisienne&display=swap" rel="stylesheet">
<style>
  :root {
    --backdrop-top: #f7f7f7;
    --backdrop-bottom: #e4e4e4;
    --page: #fbfbfc;
    --ink: #3a3631;
    --heading-ink: #2a2622;
    --frame-gold: #c9a45e;
    --burlap-dark: #7a5a36;
    --burlap-light: #a88257;
    --hops-green: #9cc04a;
    --mark-grey: #a9a9a9;
  }
  * { box-sizing: border-box; margin: 0; padding: 0; }
  html, body {
    width: 1200px; height: 986px; overflow: hidden;
    background: linear-gradient(180deg, var(--backdrop-top), var(--backdrop-bottom));
    font-family: "EB Garamond", Georgia, serif;
    color: var(--ink);
  }
  .spread {
    position: absolute; left: 38px; width: 1123px; height: 434px;
    background: var(--page);
    box-shadow: 3px 4px 6px rgba(0,0,0,0.35);
    overflow: hidden;
  }
  .spread--attractions { top: 47px; }
  .spread--lifestyle { top: 502px; height: 435px; }
  .faded-scene {
    position: absolute; inset: 0;
    background:
      radial-gradient(ellipse at 70% 45%, rgba(214,204,188,0.35), transparent 60%),
      radial-gradient(ellipse at 30% 70%, rgba(205,210,214,0.35), transparent 55%),
      linear-gradient(180deg, #fcfcfc, #f2f1ef);
  }
  .spread--lifestyle .faded-scene {
    background:
      radial-gradient(ellipse at 15% 20%, rgba(200,205,200,0.4), transparent 50%),
      radial-gradient(ellipse at 85% 40%, rgba(200,202,204,0.4), transparent 55%),
      linear-gradient(180deg, #f7f7f7, #efefef);
  }
  .burlap-panel {
    position: absolute; left: 0; top: 0; width: 197px; height: 100%;
    background:
      radial-gradient(ellipse at 30% 40%, rgba(156,192,74,0.85), rgba(156,192,74,0) 45%),
      linear-gradient(135deg, var(--burlap-light), var(--burlap-dark));
  }
  .photo {
    position: absolute;
    border: 2px solid var(--frame-gold);
  }
  .photo--dining { background: linear-gradient(135deg, #e9dcc7, #b9a078 60%, #8a7358); }
  .photo--harbor { background: linear-gradient(180deg, #5e8a45 0%, #7a9a5e 35%, #c9c3b5 55%, #8f9aa0 100%); }
  .photo--pier { background: linear-gradient(180deg, #4f7fc4 0%, #9cbce0 35%, #e6d49a 60%, #6fa6a4 80%, #e3d6bd 100%); }
  .photo--piano { background: linear-gradient(135deg, #1c1a19, #4a3a30 50%, #b9b3ab); }
  .photo--horses { background: linear-gradient(135deg, #c8c6c0, #5a4a3c 50%, #2b2a2a); }
  .photo--golf { background: linear-gradient(180deg, #6aa0d8 0%, #f4e6b5 40%, #7fae3c 65%, #4e8a2a 100%); }
  .photo--shopping { background: linear-gradient(135deg, #e9d5c0, #d7b8c8 50%, #8a9a78); }

  .title {
    position: absolute; left: 232px; top: 35px;
    font-family: "Parisienne", cursive;
    font-size: 17px; font-weight: 400; color: var(--heading-ink);
  }
  .intro {
    position: absolute; left: 232px; top: 58px; width: 300px;
    font-style: italic; font-size: 9.4px; line-height: 14px;
  }
  .section { position: absolute; }
  .section h2 {
    font-style: italic; font-weight: 600; font-size: 11px;
    color: var(--heading-ink); margin-bottom: 3px; letter-spacing: 0.1px;
  }
  .section p {
    font-size: 8.6px; line-height: 13.6px; text-align: justify;
  }
  .brand-mark {
    position: absolute; right: 20px;
    display: flex; align-items: center; gap: 4px;
    font-size: 8px; color: var(--mark-grey);
  }
  .brand-mark .dot {
    width: 6px; height: 6px; border-radius: 50%; background: var(--mark-grey);
  }
</style>
</head>
<body>

<section class="spread spread--attractions">
  <div class="faded-scene" role="img" aria-label="Faded harbor cityscape behind the text"></div>
  <div class="burlap-panel" role="img" aria-label="Green hops resting on burlap cloth"></div>

  <h1 class="title">Charleston's Attractions</h1>
  <p class="intro">Whatever your interests, the Lowcountry paradise has something for everyone. Charleston offers a multitude of unique attractions that simply must be seen.</p>

  <div class="photo photo--dining" style="left:232px; top:118px; width:288px; height:140px;" role="img" aria-label="Family sharing a meal at a restaurant"></div>

  <article class="section" style="left:232px; top:283px; width:292px;">
    <h2>Culture Meets Cuisine</h2>
    <p>Visit some of Charleston's finest eateries and meet the culinary minds behind the masterpieces. Learn about the history and evolution of Lowcountry cuisine. Enjoy samples and unlock new skills. Charleston offers a wide range of culinary tours designed to expose inhabitants and visitors to some of the area's best fare. From wine pairing tours to excursions to find the city's best deserts, there is a tour for every flavor. For those new to the area, this is an excellent way to experience local cuisine and find the area's hidden gems.</p>
  </article>

  <div class="photo photo--harbor" style="left:590px; top:45px; width:182px; height:163px;" role="img" aria-label="Red and white tugboats moored in a harbor"></div>
  <div class="photo photo--pier" style="left:590px; top:223px; width:182px; height:163px;" role="img" aria-label="Ornate pavilion on a pier over the water"></div>

  <article class="section" style="left:802px; top:49px; width:269px;">
    <h2>Learn About Marine Life</h2>
    <p>The city's expansive aquarium offers visitors a chance to enjoy the beauty of marine life first-hand. Featuring more than 5000 indigenous and exotic species of fish, reptile, and amphibians, the aquarium invites the curious and adventurous alike. Interactive exhibits encourage visitors to get up close and personal with wildlife that is rarely seen and often misunderstood. Bonnethead and cownose sharks, southern stingrays, starfish, hermit crabs, and sea urchins reside in large tanks with shallow pools that are designed to allow visitors to reach out and touch the animals. Enthusiastic and knowledgeable volunteers are always nearby to guarantee safety and provide information and insight. The facility opens into the adjoining Charleston Harbor where bottlenose dolphins and sea turtles can be observed in an intimate setting few people have the pleasure of enjoying.</p>
  </article>

  <article class="section" style="left:802px; top:259px; width:269px;">
    <h2>Art in the City</h2>
    <p>In recent decades, a powerful cultural initiative has taken root in the city. Folk art and artisan crafts remain integral elements of the Charleston art scene. Arts festivals and exhibits occur year-round and the multitude of galleries featuring original works from local and world-renowned artists is ever-expanding. Fine art galleries as well as those housing contemporary or modern works are scattered throughout the city. Open air exhibits and outdoor statue gardens provide an alternative way to experience the local culture while keeping the arts accessible to the public.</p>
  </article>

  <div class="brand-mark" style="bottom:18px;"><span class="dot"></span>Willow Crest Estate</div>
</section>

<section class="spread spread--lifestyle">
  <div class="faded-scene" role="img" aria-label="Faded palm trees and historic street behind the text"></div>

  <div class="photo photo--piano" style="left:44px; top:43px; width:163px; height:163px;" role="img" aria-label="Hands playing a grand piano"></div>
  <div class="photo photo--horses" style="left:44px; top:220px; width:163px; height:164px;" role="img" aria-label="Carriage horses on a historic street"></div>

  <article class="section" style="left:235px; top:53px; width:303px;">
    <h2>The Sound of the City</h2>
    <p>Charleston's music scene is as diverse as every other aspect of the city and the venues are nearly as important as the music itself. Visit the historic Elmstead Meeting Church for performances inspired by the Charleston's musical heritage. The group's weekly set includes gospel, jazz, slave songs, and Civil War era battle hymns. Visit a venue or, allow the music to come to you. Harborlight Chamber Ensemble is a comprised of Lowcountry musicians with a passion for classical music as well as historic tradition. The group performs classic chamber music in a variety of settings including historic homes, businesses, and concert halls throughout the region. The Lowtide Symphony Orchestra performs between September thru May offering three series ranging from classical masterpieces to light-hearted pops.</p>
  </article>

  <article class="section" style="left:235px; top:236px; width:303px;">
    <h2>Equestrian Life</h2>
    <p>Charleston boasts a rich equestrian heritage that is still visible throughout the city. A vast network of horse riding trails snake through the city, offering riders a unique view of remote portions of the landscape. Several stables and equestrian academies are active in and around the city, including the Brambleford Riding Academy on Marley Isle. Each year, Charleston County is host to The Marsh Gate Cup steeplechase along with dozens of other races, horse shows, and other events. Tidewater College's championship Equestrian Team performs throughout the season and volunteers at several community events, allowing aspiring riders access to some of the sport's leading stars.</p>
  </article>

  <div class="photo photo--golf" style="left:582px; top:43px; width:164px; height:163px;" role="img" aria-label="Gloved hand placing a golf ball on a green"></div>
  <div class="photo photo--shopping" style="left:582px; top:220px; width:164px; height:164px;" role="img" aria-label="Couple carrying shopping bags along a sunny street"></div>

  <article class="section" style="left:774px; top:31px; width:297px;">
    <h2>Tour the Historic District</h2>
    <p>There is no better way to learn about the city's rich history than to enjoy a guided tour. Most guides are locals, proud of their heritage and eager to share their expert knowledge with enthusiastic and curious minds. Although walking tours, biking tours, and guided kayak excursions are all excellent ways to see and learn about the city, perhaps no method of touring the area better captures its spirit than touring the city streets from a horse drawn carriage. The city is host to several companies offering private and group tours and. Some companies also offer the option to tour the city's famed historic sites aboard comfortable, climate-controlled mini buses.</p>
  </article>

  <article class="section" style="left:774px; top:183px; width:297px;">
    <h2>Golfing</h2>
    <p>Charleston is home to several championship golf courses designed by world renowned masters in their field. The courses are variably complex, some being suitable for novices while others offer a challenge for the most skilled golfer. The courses are beautifully crafted to seamlessly integrate with the existing landscape. Dune-spotted greens along the coast offer stunning views and unique challenges. Other courses are situated amidst the maritime forests and tidal marshes, where Spanish moss gracefully drapes the ancient southern live oaks, acting as an elegant ornament on the trees' intricate silhouettes.</p>
  </article>

  <article class="section" style="left:774px; top:326px; width:297px;">
    <h2>Enjoy Local Shopping</h2>
    <p>Upscale retail shops and trendy boutiques line the streets of Charleston's posh downtown district. Here, shoppers will find everything from imported luxury handbags to handmade jewelry. For a more authentic experience, visit Charleston's historic Magnolia Row Market and seek out souvenirs designated with the special Certified Authentic seal.</p>
  </article>

  <div class="brand-mark" style="bottom:16px;"><span class="dot"></span>Willow Crest Estate</div>
</section>

</body>
</html>
```